Brand new website for global research and investment startup

We need a simple website, maybe 3 pages: landing page with business description, investment philosophy, team and contact info.
We have a logo already that can be incorporated. Please use the logo only, not the text
We like the color green, something along the lines of #3D6C32 as the main color.
We'd like to design the website with geometric shapes in gradations of the base color. The shapes should suggest "work in progress", "built to last (a long time)", "solidity" and "indestructibility". One idea floating in my head sees smaller features with icosahedron and dodecahedron shapes, and maybe larger structures like crystal lattices; but please feel free to be creative and imagine your own.

```html
<!DOCTYPE html>
<html lang="en">
<head>
<meta charset="utf-8">
<title>Fernvale Research &amp; Investment</title>
<link href="https://fonts.googleapis.com/css2?family=Fraunces:ital,opsz,wght@0,9..144,500;0,9..144,600;1,9..144,600&family=Inter:wght@400;500;600;700&display=swap" rel="stylesheet">
<style>
:root{
  --green-dark:#2c5a2f;
  --green:#3d6c32;
  --green-bright:#4f9a3f;
  --green-pale:#a9cfa0;
  --bg:#ffffff;
  --bg-soft:#f3f6ef;
  --bg-nav:#f9f9f4;
  --text:#5d6a58;
  --text-muted:#8a9985;
  --line:#dfe5da;
  --white:#ffffff;
  --shape:rgba(61,108,50,.07);
  --shape-footer:rgba(255,255,255,.07);
}
*{box-sizing:border-box;margin:0;padding:0}
html,body{width:1200px;height:3183px;overflow:hidden}
body{background:var(--bg);font-family:"Inter",Arial,sans-serif;color:var(--text);position:relative}
.wrap{width:760px;margin-left:220px;position:relative;z-index:1}
section,footer{position:relative;overflow:hidden}
a{color:inherit;text-decoration:none}

/* soft geometric background fields */
.geo{position:absolute;z-index:0;pointer-events:none}
.geo-hero{left:720px;top:120px;width:480px;height:300px;background:linear-gradient(150deg,transparent 20%,var(--shape) 45%,var(--shape) 60%,transparent 85%)}
.geo-who{left:0;top:110px;width:215px;height:300px;background:linear-gradient(160deg,transparent 10%,var(--shape) 40%,var(--shape) 65%,transparent 90%)}
.geo-phil{left:920px;top:180px;width:280px;height:260px;background:linear-gradient(150deg,transparent 15%,var(--shape) 45%,var(--shape) 65%,transparent 90%)}
.geo-ins{left:0;top:100px;width:230px;height:280px;background:linear-gradient(160deg,transparent 10%,var(--shape) 40%,var(--shape) 65%,transparent 90%)}
.geo-team{left:950px;top:210px;width:250px;height:260px;background:linear-gradient(150deg,transparent 15%,var(--shape) 45%,var(--shape) 65%,transparent 90%)}
.geo-foot{left:970px;top:120px;width:230px;height:212px;background:linear-gradient(150deg,transparent 10%,var(--shape-footer) 45%,var(--shape-footer) 70%,transparent 95%)}

.topbar{height:20px;background:var(--green-dark);color:#dfe9da;font-size:7.5px;letter-spacing:1.6px;font-weight:600}
.topbar .wrap{display:flex;justify-content:space-between;align-items:center;height:20px}

.nav{height:62px;background:var(--bg-nav);border-bottom:3px double var(--line)}
.nav .wrap{display:flex;align-items:center;height:100%;justify-content:space-between}
.nav-links{display:flex;gap:22px;font-size:8px;letter-spacing:1.2px;color:var(--text)}
.brand{position:absolute;left:50%;transform:translateX(-50%);display:flex;align-items:center;gap:8px}
.brand-mark{width:14px;height:14px;background:var(--green-dark)}
.brand-name{font-family:"Inter",sans-serif;font-weight:700;color:var(--green-dark);font-size:14px;line-height:1.05;letter-spacing:.5px}
.brand-name small{display:block;font-size:7px;letter-spacing:3px;font-weight:700}
.btn-solid{display:inline-block;background:var(--green-dark);color:var(--white);font-size:9px;font-weight:700;letter-spacing:1.3px;padding:10px 16px}
.btn-outline{display:inline-block;border:1px solid var(--green-dark);color:var(--green-dark);font-size:9px;font-weight:700;letter-spacing:1.3px;padding:9px 15px}
.link-arrow{font-size:8.5px;font-weight:700;letter-spacing:1.2px;color:var(--green-dark);border-bottom:1px solid var(--green-dark);padding-bottom:3px}

.eyebrow{font-size:8.5px;letter-spacing:1.8px;font-weight:700;color:var(--green-bright)}
.eyebrow em{font-family:"Fraunces",serif;font-style:italic;color:var(--text-muted);font-weight:500;letter-spacing:1px;margin-right:6px}
h1,h2,h3{font-family:"Fraunces",Georgia,serif;color:var(--green-dark);font-weight:600}
h2{font-size:28px;line-height:1.12;letter-spacing:-.3px}
p.body{font-size:11px;line-height:1.8}

/* hero */
.hero{height:410px;border-bottom:1px solid var(--line)}
.hero .wrap{display:flex;padding-top:73px}
.hero-copy{width:370px}
.hero h1{font-size:36px;line-height:1.08;margin:16px 0 22px;letter-spacing:-.4px;white-space:nowrap}
.hero h1 em{color:var(--green-bright);font-style:italic}
.hero p.body{width:360px}
.hero-actions{display:flex;align-items:center;gap:13px;margin-top:24px}
.hero-stats{margin-left:85px;border-left:1px solid var(--line);padding-left:20px;width:305px;height:280px}
.stat{display:flex;align-items:center;height:65px;border-top:1px solid var(--line)}
.stat:first-child{margin-top:-2px}
.stat b{font-family:"Fraunces",serif;font-weight:600;font-size:23px;color:var(--green-bright);width:73px}
.stat span{font-size:7.8px;letter-spacing:1.4px;color:var(--text-muted);line-height:1.6;width:210px}

/* who */
.who{height:472px;border-bottom:1px solid var(--line)}
.who .wrap{display:flex;padding-top:74px}
.who-copy{width:315px}
.who h2{margin:14px 0 18px;font-size:26px;white-space:nowrap}
.who p.body{font-size:10.3px;line-height:1.7;margin-bottom:22px;width:300px}
.features{margin-left:13px;width:432px;margin-top:8px}
.feature{display:flex;gap:13px;border-bottom:1px solid var(--line);padding:18px 0}
.feature:first-child{padding-top:4px}
.feature:last-child{border-bottom:none}
.icon-box{width:30px;height:30px;border:1px solid var(--line);display:flex;align-items:center;justify-content:center;flex:none;background:var(--white)}
.feature h3{font-size:12px;margin-bottom:5px}
.feature p{font-size:9.2px;line-height:1.7;color:var(--green-bright);opacity:.85}

/* philosophy */
.philosophy{height:643px;background:var(--bg-soft);border-bottom:1px solid var(--line)}
.philosophy .wrap{padding-top:76px}
.philosophy h2{margin:15px 0 20px;width:430px}
.philosophy p.body{width:420px;font-size:10.3px;line-height:1.7}
.principles{margin-top:40px}
.principle{display:flex;align-items:flex-start;height:86px;border-bottom:1px solid var(--line);padding-top:15px}
.principle:last-child{border-bottom:none}
.principle .num{font-family:"Fraunces",serif;font-size:30px;color:var(--green-pale);width:130px;line-height:1}
.principle h3{font-size:12.5px;width:260px;padding-top:4px}
.principle p{font-size:9.2px;line-height:1.85;color:var(--text-muted);width:370px}
.philosophy .btn-outline{margin-top:30px;background:transparent}

/* insights */
.insights{height:528px;border-bottom:1px solid var(--line)}
.insights .wrap{padding-top:76px}
.insights-head{display:flex;justify-content:space-between;align-items:flex-end;margin:13px 0 30px}
.post{display:flex;align-items:flex-start;height:100px;border-bottom:1px solid var(--line);padding-top:6px}
.post:last-child{border-bottom:none}
.post-icon{width:64px;padding-top:4px}
.post-meta{width:131px;font-size:8px;font-weight:700;letter-spacing:1px;color:var(--green-bright);line-height:1.35}
.post h3{width:240px;margin-right:20px;font-size:12.5px;line-height:1.3;padding-top:4px}
.post p{width:305px;font-size:9px;line-height:1.95;color:var(--text-muted)}
.post p a{color:var(--green-dark);font-weight:700;border-bottom:1px solid var(--green-dark);padding-bottom:2px}

/* team & contact */
.team{height:716px;background:var(--bg-soft)}
.team .wrap{padding-top:76px}
.team h2{margin:13px 0 17px}
.team p.body{width:420px;font-size:10.3px;line-height:1.7}
.members{display:flex;margin-top:36px;padding-bottom:50px;border-bottom:1px solid var(--line)}
.member{display:flex;gap:12px;align-items:center;padding-right:20px;border-right:1px solid var(--line);margin-right:20px}
.member:last-child{border:none}
.initials{width:36px;height:36px;border:1px solid var(--line);display:flex;align-items:center;justify-content:center;font-family:"Fraunces",serif;font-weight:600;font-size:11px;color:var(--green-dark);background:var(--white)}
.member h3{font-size:10.5px}
.member span{font-size:8.8px;color:var(--text-muted)}
.contact{display:flex;justify-content:space-between;padding-top:38px}
.contact-copy{width:358px;padding-top:12px}
.contact h3.title{font-size:20px;margin-bottom:15px}
.contact-copy p.body{font-size:10px;line-height:1.75;width:358px}
.contact-list{margin-top:22px}
.contact-list li{list-style:none;display:flex;gap:9px;align-items:center;font-size:9px;color:var(--text);height:33px;border-bottom:1px solid var(--line)}
.contact-list li:last-child{border:none}
.form{width:361px}
.field{border-bottom:1px solid #c8d0c3;height:56px;padding-top:6px}
.field label{display:block;font-size:8px;letter-spacing:1.3px;font-weight:700;color:var(--text);margin-bottom:14px}
.field span{font-size:9px;color:#b5bdb1}
.field.tall{height:82px}
.form .btn-solid{display:block;text-align:center;margin-top:22px;padding:10px}

/* footer */
.footer{height:332px;background:var(--green-dark);color:#d9e6d4}
.footer .wrap{padding-top:50px}
.footer-cols{display:flex}
.footer-brand{width:326px}
.footer-brand .brand{position:static;transform:none}
.footer .brand-name{color:var(--white)}
.footer .brand-mark{background:var(--white)}
.footer-brand p{font-size:10px;line-height:1.75;margin:18px 0 20px;width:225px}
.footer .btn-outline{border-color:#cfe0ca;color:var(--white)}
.footer h4{font-size:8px;letter-spacing:1.6px;font-weight:700;margin-bottom:14px;color:#bcd0b5}
.footer li{list-style:none;font-size:9px;margin-bottom:9px;display:flex;gap:8px;align-items:center}
.footer-nav{width:196px}
.footer-bottom{display:flex;justify-content:space-between;margin-top:52px;border-top:1px solid #4a7448;padding-top:22px;font-size:8.5px}
.footer-bottom b{letter-spacing:1.4px;font-size:8px}
</style>
</head>
<body>

<div class="topbar"><div class="wrap"><span>INDEPENDENT EQUITY RESEARCH &amp; INVESTMENT</span><span>FOR PROFESSIONAL INVESTORS ONLY</span></div></div>

<header class="nav"><div class="wrap">
  <nav class="nav-links"><a>HOME</a><a>PHILOSOPHY</a><a>BLOG</a><a>TEAM &amp; CONTACT</a></nav>
  <div class="brand"><span class="brand-mark"></span><div class="brand-name">FERNVALE<small>RESEARCH &amp; INVESTMENT</small></div></div>
  <a class="btn-solid">REQUEST AN INTRODUCTION</a>
</div></header>

<section class="hero">
  <div class="geo geo-hero" role="img" aria-label="Faint green geometric background shape"></div>
  <div class="wrap">
  <div class="hero-copy">
    <div class="eyebrow"><em>NO. 01</em>INDEPENDENT EQUITY RESEARCH &amp; INVESTMENT</div>
    <h1>Disciplined research.<br><em>Patient capital.</em></h1>
    <p class="body">Fernvale Research &amp; Investment is an independent research-led investment firm. We study businesses the way founders do — deeply, patiently, and with a bias toward durable advantage over market noise — so capital compounds the way a stream widens as it runs its course.</p>
    <div class="hero-actions"><a class="btn-solid">REQUEST AN INTRODUCTION</a><a class="link-arrow">OUR PHILOSOPHY →</a></div>
  </div>
  <div class="hero-stats">
    <div class="stat"><b>15+</b><span>YEARS OF COMBINED RESEARCH EXPERIENCE</span></div>
    <div class="stat"><b>30–50</b><span>CONCENTRATED PORTFOLIO POSITIONS</span></div>
    <div class="stat"><b>1</b><span>INVESTMENT PHILOSOPHY, APPLIED CONSISTENTLY</span></div>
  </div>
</div></section>

<section class="who">
  <div class="geo geo-who" role="img" aria-label="Faint green geometric background shape"></div>
  <div class="wrap">
  <div class="who-copy">
    <div class="eyebrow"><em>NO. 02</em>WHO WE ARE</div>
    <h2>Research first.<br>Everything else follows.</h2>
    <p class="body">We built Fernvale Research &amp; Investment on a simple premise: markets reward the investors who understand a business better than the crowd does, and who have the patience to wait for that understanding to be recognized. We are not a mass-market product — we work face-to-face with a select group of professional investors who share our horizon and our discipline.</p>
    <a class="link-arrow">SPEAK WITH OUR TEAM →</a>
  </div>
  <div class="features">
    <div class="feature"><div class="icon-box"><svg width="20" height="14" viewBox="0 0 20 14" fill="none" stroke="#2c5a2f" stroke-width="1"><path d="M1 13h18M2 11l5-5 4 3 7-7"/></svg></div><div><h3>Primary Research</h3><p>Original, bottom-up analysis of company fundamentals, industry structure, and competitive positioning.</p></div></div>
    <div class="feature"><div class="icon-box"><svg width="20" height="20" viewBox="0 0 20 20" fill="none" stroke="#4f9a3f"><circle cx="10" cy="10" r="8" stroke-opacity=".5"/><circle cx="10" cy="10" r="5"/><circle cx="10" cy="10" r="2.5" fill="#4f9a3f"/></svg></div><div><h3>Concentrated Portfolios</h3><p>A limited number of high-conviction positions, sized to reflect our confidence, not an index weighting.</p></div></div>
    <div class="feature"><div class="icon-box"><svg width="20" height="14" viewBox="0 0 20 14" fill="none" stroke="#2c5a2f"><rect x="1" y="2" width="8" height="10"/><path d="M6 7h12M15 4l3 3-3 3"/></svg></div><div><h3>Direct Access</h3><p>A firm structured for face-to-face relationships with our investors, not broad distribution.</p></div></div>
    <div class="feature"><div class="icon-box"><svg width="18" height="18" viewBox="0 0 18 18"><path d="M9 2L16 16H2Z" fill="none" stroke="#2c5a2f"/><path d="M9 7L13 15H5Z" fill="#4f9a3f"/></svg></div><div><h3>Alignment</h3><p>We invest alongside our clients and measure ourselves by the same time horizon we ask of them.</p></div></div>
  </div>
</div></section>

<section class="philosophy">
  <div class="geo geo-phil" role="img" aria-label="Faint green geometric background shape"></div>
  <div class="wrap">
  <div class="eyebrow"><em>NO. 03</em>INVESTMENT PHILOSOPHY</div>
  <h2>Three principles, applied without exception</h2>
  <p class="body">Our approach is deliberately narrow. We would rather do a few things exceptionally well than many things adequately — the same discipline we look for in the businesses we back.</p>
  <div class="principles">
    <div class="principle"><div class="num">01</div><h3>Own Businesses, Not Tickers</h3><p>We evaluate companies as private owners would — by their economics, governance, and ability to compound capital over years, not by short-term price movement.</p></div>
    <div class="principle"><div class="num">02</div><h3>Insist on a Margin of Safety</h3><p>Every position is sized against a disciplined estimate of intrinsic value, leaving room for the analysis to be wrong without capital being permanently impaired.</p></div>
    <div class="principle"><div class="num">03</div><h3>Let the Stream Widen</h3><p>Compounding rewards patience. We resist the urge to trade around conviction and let well-chosen positions broaden in value over full market cycles.</p></div>
  </div>
  <a class="btn-outline">READ OUR FULL PHILOSOPHY</a>
</div></section>

<section class="insights">
  <div class="geo geo-ins" role="img" aria-label="Faint green geometric background shape"></div>
  <div class="wrap">
  <div class="eyebrow"><em>NO. 04</em>FROM THE RESEARCH DESK</div>
  <div class="insights-head"><h2>Recent Insights</h2><a class="link-arrow">VIEW ALL POSTS →</a></div>
  <div class="post"><div class="post-icon"><svg width="22" height="16" viewBox="0 0 22 16" stroke="#9aa896"><path d="M2 15v-4M7 15v-7M12 15v-5M17 15v-12"/></svg></div><div class="post-meta">RESEARCH NOTES<br>7 MIN READ</div><h3>What Separates a Compounder from a Cyclical Winner</h3><p>A framework for distinguishing durable competitive advantage from a temporary cyclical tailwind — and why the distinction matters more than the multiple you pay. <a>READ →</a></p></div>
  <div class="post"><div class="post-icon"><svg width="20" height="20" viewBox="0 0 20 20" fill="none" stroke="#4f9a3f"><circle cx="10" cy="10" r="8" stroke-opacity=".4"/><circle cx="10" cy="10" r="2.5" fill="#4f9a3f"/></svg></div><div class="post-meta">PORTFOLIO STRATEGY<br>5 MIN READ</div><h3>The Case for a Concentrated Portfolio</h3><p>Why owning fewer businesses, understood deeply, tends to outperform owning many, understood superficially — and how we manage the risk that comes with it. <a>READ →</a></p></div>
  <div class="post"><div class="post-icon"><svg width="22" height="16" viewBox="0 0 22 16" fill="none" stroke="#6b7a66"><path d="M1 15l6-6 4 3 9-8"/></svg></div><div class="post-meta">MARKET COMMENTARY<br>6 MIN READ</div><h3>Reading a Cycle Without Trading It</h3><p>Our view on why acknowledging where we are in a cycle need not translate into tactical trading — and how we stay anchored to fundamentals regardless. <a>READ →</a></p></div>
</div></section>

<section class="team">
  <div class="geo geo-team" role="img" aria-label="Faint green geometric background shape"></div>
  <div class="wrap">
  <div class="eyebrow"><em>NO. 05</em>TEAM &amp; CONTACT</div>
  <h2>A small team, deliberately</h2>
  <p class="body">Fernvale Research &amp; Investment is led by a compact group of analysts and portfolio managers who each carry deep sector expertise. We meet our investors directly — no intermediaries, no mass distribution — because the relationships that matter to us are built in conversation, not in a pitch deck.</p>
  <div class="members">
    <div class="member"><div class="initials">MP</div><div><h3>Managing Partner</h3><span>Investment Strategy &amp; Portfolio Management</span></div></div>
    <div class="member"><div class="initials">HR</div><div><h3>Head of Research</h3><span>Fundamental Analysis &amp; Diligence</span></div></div>
    <div class="member"><div class="initials">IR</div><div><h3>Investor Relations</h3><span>Client Partnerships &amp; Reporting</span></div></div>
  </div>
  <div class="contact">
    <div class="contact-copy">
      <h3 class="title">Request an Introduction</h3>
      <p class="body">Our work is by introduction and direct conversation. If you are a professional investor and would like to learn more about our approach, reach out — we respond personally to every inquiry.</p>
      <ul class="contact-list">
        <li><svg width="11" height="9" viewBox="0 0 11 9" fill="none" stroke="#2c5a2f"><rect x=".5" y=".5" width="10" height="8"/><path d="M1 1l4.5 4L10 1"/></svg>invest@fernvaleresearch.example</li>
        <li><svg width="11" height="11" viewBox="0 0 11 11" fill="none" stroke="#2c5a2f"><path d="M2 1l2 2-1 1.5c.8 1.6 1.9 2.7 3.5 3.5L8 7l2 2-1.5 1.5C5 10 1 6 .5 2.5Z"/></svg>+1 (212) 555-0187</li>
        <li><svg width="9" height="11" viewBox="0 0 9 11" fill="none" stroke="#2c5a2f"><path d="M4.5 10.5S1 6.5 1 4.2a3.5 3.5 0 017 0c0 2.3-3.5 6.3-3.5 6.3Z"/><circle cx="4.5" cy="4.2" r="1.2"/></svg>Boston, MA — by appointment only</li>
      </ul>
    </div>
    <div class="form">
      <div class="field"><label>FULL NAME</label><span>Jane Doe</span></div>
      <div class="field"><label>EMAIL ADDRESS</label><span>jane@firm.com</span></div>
      <div class="field"><label>FIRM / INSTITUTION</label><span>Firm name</span></div>
      <div class="field tall"><label>MESSAGE</label><span>Tell us a little about your mandate.</span></div>
      <a class="btn-solid">SEND MESSAGE</a>
    </div>
  </div>
</div></section>

<footer class="footer">
  <div class="geo geo-foot" role="img" aria-label="Faint light geometric background shape"></div>
  <div class="wrap">
  <div class="footer-cols">
    <div class="footer-brand">
      <div class="brand"><span class="brand-mark"></span><div class="brand-name">FERNVALE<small>RESEARCH &amp; INVESTMENT</small></div></div>
      <p>Fernvale Research &amp; Investment is an independent equity research and investment management firm serving select professional investors.</p>
      <a class="btn-outline">REQUEST AN INTRODUCTION</a>
    </div>
    <div class="footer-nav">
      <h4>NAVIGATE</h4>
      <ul><li>⌂ Home</li><li>▭ Investment Philosophy</li><li>▯ Blog</li><li>◦ Team &amp; Contact</li></ul>
    </div>
    <div>
      <h4>CONTACT</h4>
      <ul><li>✉ invest@fernvaleresearch.example</li><li>☏ +1 (212) 555-0187</li><li>◎ Boston, MA — by appointment only</li></ul>
    </div>
  </div>
  <div class="footer-bottom"><span>© 2026 Fernvale Research &amp; Investment. All rights reserved. For professional investors only. Not a solicitation.</span><b>BACK TO TOP ↑</b></div>
</div></footer>

</body>
</html>
```